Company or website name
- Jardin d'Aurores
- Slogan or Tagline
- No Taglines, but each description listed here needs to be on the front label of each of these wines.
- Describe your company and organization and target audience
- Consumers buying wine aged 30+, restaurants. Of wine buyers, 55% are female shopping at major grocery chains.
- The design should have the following
- The style should marry traditional sophistication with a touch of contemporary fun. It should tell knowledgeable wine buyers that it is a serious, quality product, but have enough light to attract the novice wine buyers and impulse buyers. Must have: 1) Jardin d'Aurores (brand name) 2) Method Traditionelle 3) Appellation Cremant de Limoux Controlee 4) Product of France -Brut -Brut RoseFountaine de la Vie means "Garden of Dawns" in French We would like this idea implemented into the design of the label. As a sparkling wine, bubbles are what spring from this fountain.
- This design should not have this in the entries
- No use of Gold or Gold Foil (scratches too easily). Also, black labels tend to scuff and don't travel well (plus they don't stand out on the shelves as much). Not too frilly – this is a quality product. We do not want to turn off serious wine buyers because they don’t take the label seriously.

```html
<!DOCTYPE html>
<html lang="en">
<head>
<meta charset="utf-8">
<title>Jardin d'Aurores – Brut Rosé Labels</title>
<link rel="stylesheet" href="https://fonts.googleapis.com/css2?family=Pinyon+Script&family=Questrial&family=Montserrat:wght@600&display=swap">
<style>
  :root {
    --page: #ffffff;
    --label: #f8f0e7;
    --label-edge: #e3cfc4;
    --ink: #74283f;
    --frame: #c27a89;
    --ornament: #d9a3ae;
  }
  html, body {
    margin: 0;
    padding: 0;
    width: 1200px;
    height: 960px;
    overflow: hidden;
    background: var(--page);
  }
  .canvas {
    position: relative;
    width: 1200px;
    height: 960px;
  }
  .neck-label {
    position: absolute;
    left: 446px;
    top: 132px;
    width: 308px;
    height: 168px;
  }
  .front-label {
    position: absolute;
    left: 238px;
    top: 428px;
    width: 723px;
    height: 428px;
  }
  .label-shape { fill: var(--label); stroke: var(--label-edge); stroke-width: 2; }
  .label-frame { fill: none; stroke: var(--frame); stroke-width: 3; }
  .ornament { fill: var(--ornament); }
  .caps {
    font-family: 'Questrial', sans-serif;
    fill: var(--ink);
    text-anchor: middle;
  }
  .method { font-size: 20px; letter-spacing: 0.5px; }
  .appellation { font-size: 18px; }
  .origin { font-size: 13px; }
  .brand {
    font-family: 'Pinyon Script', cursive;
    fill: var(--ink);
    font-size: 86px;
  }
  .variety {
    font-family: 'Montserrat', sans-serif;
    font-weight: 600;
    font-size: 21px;
    letter-spacing: 5px;
    fill: var(--ink);
    text-anchor: middle;
  }
</style>
</head>
<body>
<main class="canvas">

  <svg class="neck-label" viewBox="0 0 308 168" aria-label="Neck label: Brut Rose">
    <ellipse class="label-shape" cx="154" cy="84" rx="152" ry="82"/>
    <rect class="ornament" x="104" y="22" width="100" height="18" rx="9" role="img" aria-label="Scroll flourish"/>
    <text class="variety" x="154" y="92">BRUT ROSE</text>
    <rect class="ornament" x="104" y="124" width="100" height="20" rx="10" role="img" aria-label="Scroll flourish"/>
  </svg>

  <svg class="front-label" viewBox="0 0 723 428" aria-label="Front label: Jardin d'Aurores">
    <ellipse class="label-shape" cx="361.5" cy="214" rx="360" ry="212"/>
    <ellipse class="label-frame" cx="361.5" cy="218" rx="318" ry="188"/>
    <rect class="ornament" x="262" y="14" width="199" height="40" rx="18" role="img" aria-label="Fleur-de-lis scroll ornament"/>
    <text class="caps method" x="362" y="122">METHOD TRADITIONELLE</text>
    <text class="brand" x="110" y="214">Jardin</text>
    <text class="brand" x="606" y="282" text-anchor="end">d'Aurores</text>
    <text class="caps appellation" x="362" y="338">APPELLATION CREMANT DE LIMOUX CONTROLEE</text>
    <text class="caps origin" x="362" y="370">PRODUCT OF FRANCE</text>
    <rect class="ornament" x="328" y="392" width="67" height="24" rx="11" role="img" aria-label="Small fleur-de-lis ornament"/>
  </svg>

</main>
</body>
</html>
```